New Business Cards for Torvin Group

We need a new Business Card to compliment our new logo. We are a vibrant design, manufacture and install business providing recreation areas, public parks and Municipal spaces. We want business cards that are classy, modern and clean.

We have recently changed our logo, and are celebrating our 40th anniversary. We want business cards with a new modern design to reflect our status.

Target Market(s)

Customers

Contact Information for Business Card

We need all the details of our 3 offices as per the business card attached. Please disregard the old logo on the business card, the other three files show our new logo.

Requirements
Must have
• All info as per attached business card but with new logo.
Nice to have

```html
<!DOCTYPE html>
<html lang="en">
<head>
<meta charset="utf-8">
<title>Torvin Group – Business Card</title>
<link href="https://fonts.googleapis.com/css2?family=Roboto:wght@400;500;700&display=swap" rel="stylesheet">
<style>
  :root {
    --backdrop: #2a2a2a;
    --card-top: #1a1a1a;
    --card-bottom: #0c0c0c;
    --accent: #e8262f;
    --text-light: #e6e6e6;
    --text-muted: #9a9a9a;
    --logo-grey: #5a5a5a;
    --rule: #444444;
  }
  * { margin: 0; padding: 0; box-sizing: border-box; }
  html, body {
    width: 1200px; height: 900px; overflow: hidden;
    background: var(--backdrop);
    font-family: 'Roboto', sans-serif;
  }
  .canvas { position: relative; width: 1200px; height: 900px; }

  .card {
    position: absolute;
    width: 560px; height: 320px;
    background: linear-gradient(160deg, var(--card-top), var(--card-bottom));
    box-shadow: 0 12px 30px rgba(0,0,0,0.45);
    overflow: hidden;
  }
  .card::after {
    content: ""; position: absolute; left: 0; right: 0; bottom: 0;
    height: 12px; background: var(--accent);
  }

  /* Back: office directory */
  .card--back { left: 420px; top: 80px; }
  .offices {
    position: absolute; left: 0; right: 0; top: 30px;
    text-align: center; color: var(--text-light);
    font-size: 13.5px; line-height: 17px;
  }
  .office + .office { margin-top: 9px; padding-top: 9px; position: relative; }
  .office + .office::before {
    content: ""; position: absolute; top: 0; left: 50%;
    width: 150px; margin-left: -75px; height: 1px; background: var(--rule);
  }
  .office__title { color: var(--accent); font-weight: 700; font-size: 16px; line-height: 20px; }
  .label { color: var(--accent); font-weight: 700; }

  /* Front: identity */
  .card--front { left: 200px; top: 500px; }
  .brand {
    position: absolute; left: 56px; top: 114px;
    display: flex; align-items: center; gap: 14px;
  }
  .brand__dot { width: 56px; height: 56px; border-radius: 50%; background: var(--accent); flex: none; }
  .brand__name {
    display: flex; flex-direction: column;
    font-weight: 700; font-size: 30px; letter-spacing: 1px;
    color: var(--logo-grey); text-transform: uppercase; line-height: 31px;
  }
  .divider {
    position: absolute; left: 300px; top: 80px;
    width: 1px; height: 130px; background: var(--rule);
  }
  .person { position: absolute; left: 322px; top: 92px; }
  .person__name {
    color: var(--accent); font-size: 19px; font-weight: 500;
    text-transform: uppercase; letter-spacing: 0.3px;
  }
  .person__role { color: var(--text-muted); font-size: 14px; margin-top: 1px; }
  .contacts { list-style: none; margin-top: 20px; color: var(--text-muted); font-size: 14px; }
  .contacts li { display: flex; align-items: center; gap: 8px; line-height: 20px; }
  .contacts svg { width: 12px; height: 12px; flex: none; }
</style>
</head>
<body>
<main class="canvas">

  <section class="card card--back" aria-label="Business card back">
    <div class="offices">
      <div class="office">
        <div class="office__title">Head Office</div>
        <div>P.O.Box:41820 Abu Dhabi,U.A.E.</div>
        <div><span class="label">P :</span> +971 (0)2 5873120 | <span class="label">F :</span> +971 (0)2 5873121</div>
        <div><span class="label">E :</span> sales@torvingroup.com</div>
      </div>
      <div class="office">
        <div class="office__title">Dubai Office</div>
        <div>P.O.Box:276410 Dubai,U.A.E.</div>
        <div><span class="label">P :</span> +971 (0)4 3302847 | <span class="label">F :</span> +971 (0)4 3302848</div>
        <div><span class="label">E :</span> sales@torvingroup.com</div>
      </div>
      <div class="office">
        <div class="office__title">Qatar Office</div>
        <div>P.O.Box:20937 Doha, Qatar</div>
        <div><span class="label">P :</span> +974 44718356 | <span class="label">F :</span> +974 44718357</div>
        <div><span class="label">E :</span> sales@torvingroup.com</div>
      </div>
    </div>
  </section>

  <section class="card card--front" aria-label="Business card front">
    <div class="brand">
      <span class="brand__dot"></span>
      <span class="brand__name"><span>Torvin</span><span>Group</span></span>
    </div>
    <div class="divider"></div>
    <div class="person">
      <div class="person__name">Rami Halvorsen</div>
      <div class="person__role">Managing Partner</div>
      <ul class="contacts">
        <li>
          <svg viewBox="0 0 12 12" aria-hidden="true"><path fill="#e8262f" d="M2.5 1 4.5 1 5.2 3.6 4 4.6C4.6 6 6 7.4 7.4 8L8.4 6.8 11 7.5 11 9.5C11 10.3 10.3 11 9.5 11 5 11 1 7 1 2.5 1 1.7 1.7 1 2.5 1Z"/></svg>
          +971 (0)50 318 7740
        </li>
        <li>
          <svg viewBox="0 0 12 12" aria-hidden="true"><rect x="0.5" y="2" width="11" height="8" fill="#e8262f"/><path d="M0.8 2.4 6 6.6 11.2 2.4" fill="none" stroke="#111" stroke-width="1"/></svg>
          rami@torvingroup.com
        </li>
        <li>
          <svg viewBox="0 0 12 12" aria-hidden="true"><circle cx="6" cy="6" r="5.5" fill="#e8262f"/><path d="M0.5 6H11.5M6 0.5C3.5 3 3.5 9 6 11.5M6 0.5C8.5 3 8.5 9 6 11.5" fill="none" stroke="#111" stroke-width="0.8"/></svg>
          www.torvingroup.com
        </li>
      </ul>
    </div>
  </section>

</main>
</body>
</html>
```